Fitness business need 3x3 card to promote 6wk boot camp nutrition challenge

Hi, we're looking for someone to make our current card look better and more modern. We want to keep the text the same, but we want a better design. We also want to keep the woman on the front of the card. The card is for both men and women so we want it to feel inclusive and bright. The idea is to make the card look more modern. We want some pops of color. The main feature is to promote the pricing on the back of the card. It would be nice if that continues to look like a coupon or if it stands out with a bright color or background.

Target Market(s)

Men and women looking to get in shape

Industry/Entity Type

Fitness

Font styles to use
Serif
Sans Serif

Colors
3176b5
0255a3
33a6d7
f37122
ec1f27

Requirements
Must have
• front and back, use pic of women provided

```html
<!DOCTYPE html>
<html lang="en">
<head>
<meta charset="utf-8">
<title>Boot Camp Card – Front</title>
<link rel="stylesheet" href="https://fonts.googleapis.com/css2?family=Montserrat:wght@200;300;600;700;800&display=swap">
<style>
  :root {
    --red: #ec1f27;
    --orange: #f37122;
    --blue: #3176b5;
    --blue-deep: #0255a3;
    --blue-light: #33a6d7;
    --salmon: #f0a088;
    --white: #ffffff;
    --label-grey: #bcbec0;
  }
  * { margin: 0; padding: 0; box-sizing: border-box; }
  html, body { width: 1200px; height: 1200px; overflow: hidden; background: var(--white); }
  body { position: relative; font-family: "Montserrat", Arial, sans-serif; color: var(--white); }

  .card { position: absolute; left: 67px; top: 34px; width: 1066px; height: 1069px; overflow: hidden; }
  .card-art { position: absolute; inset: 0; width: 100%; height: 100%; }

  .title, .challenge, .dates, .site-url, .brand, .arrow-mark { position: absolute; }

  .title { left: 82px; top: 92px; line-height: 1; }
  .title-main { display: block; font-weight: 700; font-size: 128px; letter-spacing: -3px; }
  .title-sub { display: block; font-weight: 200; font-size: 60px; letter-spacing: -1px; margin-top: 2px; }

  .challenge { left: 0; top: 0; width: 100%; height: 100%; pointer-events: none; }
  .challenge > span { position: absolute; line-height: 1; white-space: nowrap; }
  .challenge-number { left: 170px; top: 800px; font-weight: 600; font-size: 180px; letter-spacing: -4px; }
  .challenge-week { left: 283px; top: 828px; font-weight: 800; font-size: 70px; letter-spacing: -2px; }
  .challenge-kicker { left: 292px; top: 893px; font-weight: 300; font-size: 19px; }
  .challenge-name { left: 288px; top: 912px; font-weight: 700; font-size: 33px; letter-spacing: -0.5px; }

  .arrow-mark { left: 533px; top: 838px; width: 56px; height: 108px; }

  .dates { left: 585px; top: 0; width: 400px; height: 100%; }
  .dates > span { position: absolute; left: 0; width: 100%; text-align: center; line-height: 1; white-space: nowrap; }
  .dates-line { font-weight: 200; font-size: 46px; letter-spacing: -1px; }
  .dates-line strong { font-weight: 700; }
  .dates-first { top: 826px; }
  .dates-to { top: 874px; font-weight: 700; font-size: 30px; color: var(--salmon); }
  .dates-second { top: 906px; }

  .site-url { left: 0; width: 1110px; top: 1002px; text-align: center; font-weight: 600; font-size: 29px; }

  .brand { left: 837px; top: 104px; width: 184px; height: 184px; display: flex; align-items: center; justify-content: center; }
  .brand-ring { position: absolute; inset: 0; border: 3px solid var(--white); border-radius: 50%; }
  .brand-name { font-weight: 600; font-size: 28px; text-align: center; line-height: 1.05; }

  .cut-line { position: absolute; left: 0; right: 0; top: 1118px; border-top: 2px dashed var(--label-grey); }
  .side-label { position: absolute; left: 0; right: 0; top: 1128px; text-align: center; font-weight: 700; font-size: 64px; color: var(--label-grey); letter-spacing: 1px; }
</style>
</head>
<body>
  <section class="card">
    <svg class="card-art" viewBox="0 0 1332 1336" preserveAspectRatio="none">
      <defs>
        <linearGradient id="bgTop" x1="0" y1="0" x2="1" y2="0.2">
          <stop offset="0" stop-color="#e63a28"/>
          <stop offset="0.6" stop-color="#cf5a48"/>
          <stop offset="1" stop-color="#a86464"/>
        </linearGradient>
        <linearGradient id="bgMid" x1="0" y1="0" x2="1" y2="0">
          <stop offset="0" stop-color="#d86a48"/>
          <stop offset="0.55" stop-color="#a07080"/>
          <stop offset="1" stop-color="#3a78c0"/>
        </linearGradient>
        <linearGradient id="bgLow" x1="0" y1="0" x2="1" y2="0">
          <stop offset="0" stop-color="#ec5a2a"/>
          <stop offset="1" stop-color="#e03a34"/>
        </linearGradient>
        <linearGradient id="bgStrip" x1="0" y1="0" x2="1" y2="0">
          <stop offset="0" stop-color="#e0603a"/>
          <stop offset="0.6" stop-color="#a06a78"/>
          <stop offset="1" stop-color="#3176b5"/>
        </linearGradient>
        <linearGradient id="photoTone" x1="0" y1="0" x2="1" y2="1">
          <stop offset="0" stop-color="#a9a9ab"/>
          <stop offset="0.5" stop-color="#6e6e70"/>
          <stop offset="1" stop-color="#2e2e30"/>
        </linearGradient>
      </defs>
      <rect width="1332" height="1336" fill="url(#bgTop)"/>
      <polygon points="0,648 1332,216 1332,1336 0,1336" fill="url(#bgMid)"/>
      <g role="img" aria-label="Black and white photo of a fit woman seated on the floor, arm resting on a medicine ball">
        <circle cx="341" cy="718" r="225" fill="#2b2b2d"/>
        <rect x="626" y="112" width="660" height="910" rx="180" fill="url(#photoTone)"/>
      </g>
      <polygon points="0,1048 1332,608 1332,1238 0,1238" fill="url(#bgLow)" opacity="0.9"/>
      <rect x="0" y="1238" width="1332" height="98" fill="url(#bgStrip)"/>
    </svg>

    <h1 class="title">
      <span class="title-main">BOOT</span>
      <span class="title-sub">CAMP TITLE</span>
    </h1>

    <div class="brand">
      <span class="brand-ring"></span>
      <span class="brand-name">YOUR<br>LOGO</span>
    </div>

    <div class="challenge">
      <span class="challenge-number">6</span>
      <span class="challenge-week">WEEK</span>
      <span class="challenge-kicker">FITNESS &amp; NUTRITION</span>
      <span class="challenge-name">CHALLENGE</span>
    </div>

    <svg class="arrow-mark" viewBox="0 0 56 108" aria-hidden="true">
      <polygon points="0,0 56,54 0,108" fill="#f0a088" opacity="0.9"/>
    </svg>

    <p class="dates">
      <span class="dates-line dates-first">OCTOBER <strong>2ND</strong></span>
      <span class="dates-to">TO</span>
      <span class="dates-line dates-second">NOVEMBER <strong>11TH</strong></span>
    </p>

    <p class="site-url">www.NorthPeakFit.com/landingpage</p>
  </section>

  <div class="cut-line"></div>
  <p class="side-label">FRONT</p>
</body>
</html>
```